Penny Harvest

Logo and general packaging design for premium quality, price conscious super foods.

Initial product portfolio includes:

Organic Raw Chia Seeds - Resealable plastic bags with 3 x 5 label.
Organic Cold Pressed Coconut Oil (plastic jar) - 2.5 x 6.5 label

The design should be transferable to additional products.

Project requirements:

The design should be simple and the core trade dress should be no more than 2 or 3 colors. The logo should reproduce well in black/1 color.

The idea of this design is to convey quality and simplicity, like a "no frills", premium quality brand.

Deliverable: fully editable (text and illustration):

Logo.

Basic Jar label design.

Basic Bag label design.

Target Market(s)

Educated women aged 22-45

Industry/Entity Type

Plastic

Requirements
Must have
• Clear, simple logo, delivered in vector form, 1 color/black.
• Use of logo on 1 jar label and 1 bag label, each with product name and space for required and optional marketing content.
Nice to have
• Additional iterations of the design to demonstrate your concept of how we will visually vary additional items in jars and bags.
• i.e. What an additional product in a bag would look like for purposes of brand consistency and product differentiation on shelf or online in e-store.
Should not have
• overly detailed graphics that don't scale well and/or may be hard to read or understand. 4 color design elements (except to simiulate how the product may look through the clear jar or bag or how the product may be placed in a simulated surrounding or ad.

```html
<!DOCTYPE html>
<html lang="en">
<head>
<meta charset="utf-8">
<title>Organic Product Labels</title>
<link href="https://fonts.googleapis.com/css2?family=Italianno&display=swap" rel="stylesheet">
<style>
  :root {
    --page: #f4f4f4;
    --ink: #262626;
    --paper: #ffffff;
    --paper-shade: #e6e6e6;
    --coconut: #8a5a32;
    --chia: #5e5247;
    --ornament: #3a3a3a;
  }
  html, body {
    margin: 0;
    padding: 0;
    width: 1200px;
    height: 1000px;
    overflow: hidden;
    background: var(--page);
  }
  .canvas {
    position: relative;
    width: 1200px;
    height: 1000px;
  }
  .label {
    position: absolute;
    display: block;
  }
  .label--jar { left: 67px; top: 38px; }
  .label--bag { left: 208px; top: 490px; }
  .product-name {
    font-family: "Italianno", cursive;
    fill: var(--ink);
  }
</style>
</head>
<body>
<main class="canvas">

  <!-- Jar label: coconut oil -->
  <svg class="label label--jar" width="1070" height="412" viewBox="0 0 1070 412" aria-label="Organic Cold Pressed Coconut Oil jar label">
    <defs>
      <linearGradient id="paperJar" x1="0" y1="0" x2="0.6" y2="0.8">
        <stop offset="0" stop-color="var(--paper-shade)"/>
        <stop offset="0.4" stop-color="var(--paper)"/>
      </linearGradient>
    </defs>
    <rect class="label-paper" width="1070" height="412" fill="url(#paperJar)"/>
    <g class="frame" fill="var(--ink)">
      <path d="M50 20 L1040 18 L1040 28 L50 30 Z"/>
      <path d="M25 26 L33 26 L31 195 L27 195 Z"/>
      <path d="M1036 24 L1046 24 L1044 262 L1038 262 Z"/>
    </g>
    <rect class="ornament" x="850" y="45" width="90" height="80" rx="30" fill="var(--ornament)" opacity="0.35" role="img" aria-label="Flourished tree ornament"/>
    <text class="product-name" x="53" y="176" font-size="98" textLength="940" lengthAdjust="spacingAndGlyphs">Organic Cold Pressed Coconut Oil</text>
    <ellipse class="product-photo" cx="922" cy="238" rx="68" ry="48" fill="var(--coconut)" role="img" aria-label="Photo of a whole and a halved coconut"/>
    <g class="waves">
      <path d="M0 212 Q300 255 640 292 L0 292 Z" fill="var(--ink)"/>
      <path d="M0 290 Q420 332 1070 296 L1070 412 L0 412 Z" fill="var(--ink)"/>
      <path d="M0 270 Q320 300 640 292" stroke="var(--paper)" stroke-width="4" fill="none"/>
      <path d="M520 380 Q800 310 1070 312" stroke="var(--paper)" stroke-width="5" fill="none"/>
      <path d="M640 392 Q860 378 1070 396" stroke="var(--paper)" stroke-width="4" fill="none"/>
    </g>
    <g class="quality-seal">
      <circle cx="70" cy="350" r="46" fill="var(--paper)"/>
      <circle cx="70" cy="350" r="38" fill="none" stroke="var(--ink)" stroke-width="4"/>
    </g>
  </svg>

  <!-- Bag label: chia seeds -->
  <svg class="label label--bag" width="787" height="472" viewBox="0 0 787 472" aria-label="Organic Raw Chia Seeds bag label">
    <defs>
      <linearGradient id="paperBag" x1="0" y1="0" x2="0.6" y2="0.8">
        <stop offset="0" stop-color="var(--paper-shade)"/>
        <stop offset="0.4" stop-color="var(--paper)"/>
      </linearGradient>
    </defs>
    <rect class="label-paper" width="787" height="472" fill="url(#paperBag)"/>
    <g class="frame" fill="var(--ink)">
      <path d="M35 20 L770 18 L770 28 L35 30 Z"/>
      <path d="M25 26 L33 26 L31 250 L27 250 Z"/>
      <path d="M756 24 L766 24 L764 262 L758 262 Z"/>
    </g>
    <rect class="ornament" x="497" y="55" width="80" height="75" rx="28" fill="var(--ornament)" opacity="0.35" role="img" aria-label="Flourished tree ornament"/>
    <text class="product-name" x="54" y="195" font-size="98" textLength="660" lengthAdjust="spacingAndGlyphs">Organic Raw Chia Seeds</text>
    <ellipse class="product-photo" cx="612" cy="275" rx="118" ry="58" fill="var(--chia)" role="img" aria-label="Photo of a heap of chia seeds"/>
    <g class="waves">
      <path d="M0 282 Q260 300 470 352 L0 352 Z" fill="var(--ink)"/>
      <path d="M0 350 Q360 390 787 356 L787 472 L0 472 Z" fill="var(--ink)"/>
      <path d="M0 336 Q260 355 470 352" stroke="var(--paper)" stroke-width="4" fill="none"/>
      <path d="M380 440 Q600 368 787 372" stroke="var(--paper)" stroke-width="5" fill="none"/>
      <path d="M470 452 Q640 440 787 456" stroke="var(--paper)" stroke-width="4" fill="none"/>
    </g>
    <g class="quality-seal">
      <circle cx="63" cy="428" r="46" fill="var(--paper)"/>
      <circle cx="63" cy="428" r="38" fill="none" stroke="var(--ink)" stroke-width="4"/>
    </g>
  </svg>

</main>
</body>
</html>
```